Velmorytrips.com web design project + logo design

Hi,

We are a Russian online tour operator - roamquiltex.com

We are looking to tranmsfer our domain to velmorytrips.com. The website and logo need to be velmoryesque - we are not looking to change our functionality, but we need to make the website much more attracitve to clients, much more wild looking but at the same time remaining a professional travel company.

The main concept of the website should be innovative travel (as velmory was an innovator). Alternatively, you could go down the artist route and go down the draw / design your own tour road.

On our website the customer is able to combine travel services (hotels, flights, Visa services, and soon chauffeur, car rental etc...) put it into their basket (the basket definitely has to look better than it is at the moment) and pay for it in one go by card.

We are also stressin our customer support with web chat, call centre etc... (call centre number at the top of the page)

We aim to provide an easy user experience, but we need to make it have some more style, so I will be waiting for what you guys can come up with.
Let me know if you have any questions - skype is: mrkostelin

Industry/Entity Type

It Company

Logo Text

Requirements
Must have
• It is quite a simple task - to take the existing website roamquiltex.com and velmorysize it to create velmorytrips.com, the functionality of the website will remain the same and there are not many pages in the website. Homepage, Checkout step1, Checkout step 2 (you can view both of these if you select a service) and the generic pages for T&C''s, Privacy policy etc...

IMPORTANT UPDATE

We are also looking at how the search results will look in the designs, (please do a search on our website for hotel / flight)

```html
<!DOCTYPE html>
<html lang="en">
<head>
<meta charset="utf-8">
<title>velmorytravel</title>
<link href="https://fonts.googleapis.com/css2?family=Cabin:wght@400;500;600;700&family=Montserrat:wght@600;700;800&family=Arimo:wght@400;700&display=swap" rel="stylesheet">
<style>
:root{
  --orange:#ee8433;
  --orange-dark:#d96f1f;
  --ink:#353535;
  --ink-soft:#555;
  --grey:#8a8a8a;
  --grey-light:#bdbdbd;
  --page:#f1f1f1;
  --white:#fff;
  --stripe:#9a9a9a;
}
*{box-sizing:border-box;margin:0;padding:0}
html,body{width:1200px;height:1176px;overflow:hidden}
body{position:relative;background:radial-gradient(ellipse at 50% 40%,#fafafa 0%,#ececec 75%);font-family:"Cabin",sans-serif;color:var(--ink)}
.abs{position:absolute}

/* top bar */
.topnav .item{position:absolute;top:20px;color:var(--ink-soft);line-height:1}
.topnav .small{font-size:12px;letter-spacing:.3px}
.topnav .big{font-family:"Arimo",sans-serif;font-size:21px;letter-spacing:-.5px;margin-top:1px}
.topnav .sep{position:absolute;top:18px;width:0;height:46px;border-left:1px dotted #bbb}
.topnav .hours{font-size:10px;color:#999;margin-top:2px}
.rule{position:absolute;left:202px;top:78px;width:798px;border-top:1px dotted #aaa}

.brand{position:absolute;left:202px;top:96px;font-family:"Cabin",sans-serif;font-weight:600;font-size:44px;letter-spacing:-1.5px;color:var(--orange)}

.landmarks{position:absolute;left:166px;top:144px;width:906px;height:232px;background:linear-gradient(180deg,rgba(200,200,200,0) 0%,rgba(190,190,190,.5) 60%,rgba(170,170,170,.65) 100%);border-radius:40px 40px 0 0}

/* booking */
.frame{position:absolute;left:210px;top:372px;width:784px;height:294px;border-radius:26px;background:var(--grey-light)}
.basket{position:absolute;left:216px;top:378px;width:176px;height:282px;border-radius:22px;background:var(--orange);overflow:hidden}
.basket .well{position:absolute;left:5px;top:70px;width:166px;height:200px;background:var(--white)}
.dark-tab{position:absolute;background:var(--ink);border-radius:14px}
.dark-tab::after{content:"";position:absolute;inset:3px;border:1.5px dashed #bbb;border-radius:12px}
.basket .dark-tab{left:10px;top:9px;width:160px;height:53px}
.tab-label{position:absolute;font-family:"Montserrat",sans-serif;font-weight:700;color:var(--white);font-size:15px}
.empty{position:absolute;left:0;width:166px;text-align:center;color:var(--orange);font-weight:600;font-size:15px;letter-spacing:.5px}
.bar{position:absolute;left:5px;width:166px;height:32px;background:repeating-linear-gradient(135deg,#a6a6a6 0 2px,#939393 2px 4px);color:var(--white);font-size:13.5px;padding-left:44px;line-height:32px}
.bar svg{position:absolute;left:14px;top:7px}

.search-panel{position:absolute;left:398px;top:376px;width:591px;height:286px;border-radius:22px;background:var(--orange)}
.search-panel .dark-tab{left:4px;top:8px;width:579px;height:58px}
.tabs span{position:absolute;top:28px;font-family:"Montserrat",sans-serif;font-weight:700;font-size:15px}
.tabs .sep{position:absolute;top:28px;height:18px;border-left:1px solid #666}
.lbl{position:absolute;color:var(--white);font-weight:600;font-size:12.5px;text-align:right;white-space:nowrap}
.lbl.left{right:499px}
.lbl.right{right:229px}
.field{position:absolute;height:26px;background:var(--white);border-radius:3px;font-size:11px;color:#444;line-height:26px;padding-left:9px}
.field svg{position:absolute;right:8px;top:7px}
.sel{position:absolute;top:174px;width:38px;height:25px;background:var(--white);border-radius:3px;font-size:11px;line-height:25px;padding-left:8px}
.sel i,.field i{position:absolute;right:4px;top:6px;width:14px;height:14px;background:#444;border-radius:2px}
.sel i::after,.field i::after{content:"";position:absolute;left:3px;top:5px;border-left:4px solid transparent;border-right:4px solid transparent;border-top:5px solid #fff}
.opt{position:absolute;font-size:9.5px;color:var(--ink)}
.box{display:inline-block;width:11px;height:11px;border-radius:2px;background:var(--ink);vertical-align:-2px;margin-right:6px}
.pill{position:absolute;left:24px;top:230px;width:156px;height:33px;border-radius:12px;background:var(--white);box-shadow:0 0 0 2px #fff,0 0 0 3px #ddd;text-align:center;line-height:33px;font-family:"Arimo",sans-serif;font-size:18px;color:var(--ink)}
.search-btn{position:absolute;left:317px;top:216px;width:255px;height:53px;border-radius:16px;background:var(--ink);box-shadow:0 0 0 3px var(--orange),0 0 0 5px #fff;text-align:center;line-height:53px;font-family:"Arimo",sans-serif;font-size:35px;letter-spacing:-1px;color:var(--white)}

/* services */
.service-head{position:absolute;top:704px;width:252px;height:60px;border-radius:14px;background:var(--ink)}
.service-head::after{content:"";position:absolute;inset:4px;border:1.5px dashed #aaa;border-radius:12px}
.service-head .name{position:absolute;top:20px;font-family:"Montserrat",sans-serif;font-weight:800;font-size:16px;color:var(--white);letter-spacing:-.3px}
.service-card{position:absolute;top:770px;width:254px;height:156px;border-radius:14px;background:var(--white);border:1px solid #e2e2e2;box-shadow:0 8px 8px -6px rgba(0,0,0,.12)}
.service-card h3{position:absolute;top:14px;left:0;width:100%;text-align:center;font-weight:500;font-size:12px;color:var(--orange)}
.service-card p,.service-card ol{position:absolute;left:25px;width:210px;font-size:9.8px;line-height:12.5px;color:var(--ink)}
.service-card ol{list-style:none;font-size:11px;line-height:22px;top:46px}
.service-card .more{position:absolute;left:20px;top:118px;font-size:10px;color:var(--ink)}

/* footer */
.footer{position:absolute;left:0;top:960px;width:1200px;height:216px;background:linear-gradient(180deg,#fff 0%,#fff 40%,#ececec 100%)}
.col{position:absolute;top:36px}
.col h4{font-weight:500;font-size:14.5px;color:#777;letter-spacing:-.2px;margin-bottom:9px}
.col li{list-style:none;font-size:10.5px;color:#777;letter-spacing:.6px;height:20px}
.col address{font-style:normal;font-size:10.5px;color:#777;letter-spacing:.6px;line-height:14.5px}
.vsep{position:absolute;top:30px;height:118px;border-left:1px dotted #ccc}
.social{display:flex;gap:6px;margin-top:4px}
.social span{width:12px;height:12px;border-radius:3px;background:var(--ink)}
.email{position:absolute;left:804px;top:1037px;width:194px;height:25px;border-radius:3px;background:#ccc;font-size:10.5px;color:#555;line-height:25px;padding-left:12px;letter-spacing:.3px}
.subscribe{position:absolute;left:805px;top:1071px;width:81px;height:20px;background:var(--ink);color:#fff;font-size:10.5px;line-height:20px;text-align:center;letter-spacing:.3px}
.copy{position:absolute;left:214px;top:1133px;font-size:11.5px;color:#777}
.copy b{font-weight:600;color:var(--orange);font-size:14px;letter-spacing:-.5px}
</style>
</head>
<body>

<nav class="topnav">
  <svg class="abs" style="left:270px;top:27px" width="26" height="26" viewBox="0 0 26 26"><path d="M3 2h20a2 2 0 0 1 2 2v12a2 2 0 0 1-2 2H11l-6 6v-6H3a2 2 0 0 1-2-2V4a2 2 0 0 1 2-2z" fill="#555"/></svg>
  <div class="item" style="left:304px"><div class="small">OUR</div><div class="big">FORUM</div></div>
  <div class="sep" style="left:392px"></div>
  <svg class="abs" style="left:409px;top:28px" width="30" height="20" viewBox="0 0 30 20"><rect width="30" height="20" fill="#555"/><path d="M0 0L30 20M30 0L0 20" stroke="#ddd" stroke-width="3"/><path d="M15 0v20M0 10h30" stroke="#ddd" stroke-width="6"/><path d="M15 0v20M0 10h30" stroke="#555" stroke-width="3"/></svg>
  <div class="item" style="left:450px"><div class="small">SELECT YOUR</div><div class="big">LANAGUE</div></div>
  <div class="sep" style="left:566px"></div>
  <svg class="abs" style="left:584px;top:26px" width="24" height="24" viewBox="0 0 24 24"><path d="M3 3l18 9-18 9 4-9z" fill="#555"/></svg>
  <div class="item" style="left:614px"><div class="small">REVIEW</div><div class="big">MY TOUR</div></div>
  <div class="sep" style="left:718px"></div>
  <svg class="abs" style="left:733px;top:25px" width="24" height="24" viewBox="0 0 24 24"><path d="M6 2l4 5-2 3c1 3 3 5 6 6l3-2 5 4-3 4C10 21 3 14 2 5z" fill="#555"/></svg>
  <div class="item" style="left:766px"><div class="small">Call Now Today</div><div class="big">+7 (495) 555-01-42</div><div class="hours">(Mon-Fri) Hours: 9:00 am - 18:00</div></div>
</nav>
<div class="rule"></div>

<div class="brand">velmorytravel</div>

<div class="landmarks" role="img" aria-label="Grey sketch of world landmarks: statue on a hill, pyramids, domed palace, clock tower, iron tower, TV tower, step pyramid and a torch statue, with an orange plane flying by"></div>

<section class="frame"></section>

<section class="basket">
  <div class="dark-tab"></div>
  <div class="tab-label" style="left:29px;top:27px">Basket</div>
  <div class="well">
    <svg class="abs" style="left:51px;top:13px" width="66" height="56" viewBox="0 0 66 56"><path d="M20 20L33 3 46 20" fill="none" stroke="#ee8433" stroke-width="5" stroke-linecap="round"/><path d="M4 20h58l-7 28a6 6 0 0 1-6 5H17a6 6 0 0 1-6-5z" fill="#ee8433"/><g fill="#fff"><rect x="17" y="28" width="5" height="18" rx="2"/><rect x="27" y="28" width="5" height="18" rx="2"/><rect x="37" y="28" width="5" height="18" rx="2"/><rect x="47" y="28" width="5" height="18" rx="2"/></g></svg>
    <div class="empty" style="top:74px">EMPTY</div>
  </div>
  <div class="bar" style="top:194px"><svg width="18" height="18" viewBox="0 0 18 18"><rect x="1" y="1" width="16" height="16" fill="none" stroke="#fff" stroke-width="1.5"/><text x="9" y="13.5" font-size="12" text-anchor="middle" fill="#fff" font-family="Arimo">$</text></svg>Payment</div>
  <div class="bar" style="top:228px"><svg width="20" height="18" viewBox="0 0 20 18"><path d="M2 10l8-8h8v8l-8 8z" fill="#fff"/><circle cx="14" cy="6" r="1.8" fill="#999"/></svg>* Price</div>
</section>

<section class="search-panel">
  <div class="dark-tab"></div>
  <div class="tabs">
    <span style="left:31px;color:#fff">Tickets</span>
    <i class="sep" style="left:110px"></i>
    <span style="left:130px;color:#aaa">Info</span>
    <i class="sep" style="left:180px"></i>
    <span style="left:198px;color:#aaa">Hotels</span>
  </div>

  <div class="lbl left" style="top:95px">Whence</div>
  <div class="field" style="left:103px;top:89px;width:166px">Type...</div>
  <div class="lbl left" style="top:128px">There</div>
  <div class="field" style="left:103px;top:122px;width:166px">30-5-2013<svg width="12" height="11" viewBox="0 0 12 11"><rect width="12" height="11" rx="1" fill="#444"/><g fill="#fff"><rect x="2" y="4" width="2" height="2"/><rect x="5" y="4" width="2" height="2"/><rect x="8" y="4" width="2" height="2"/><rect x="2" y="7" width="2" height="2"/><rect x="5" y="7" width="2" height="2"/><rect x="8" y="7" width="2" height="2"/></g></svg></div>

  <div class="lbl right" style="top:95px">Where</div>
  <div class="field" style="left:370px;top:89px;width:166px">Type...</div>
  <div class="lbl right" style="top:128px">Back</div>
  <div class="field" style="left:370px;top:122px;width:166px">16-6-2013<svg width="12" height="11" viewBox="0 0 12 11"><rect width="12" height="11" rx="1" fill="#444"/><g fill="#fff"><rect x="2" y="4" width="2" height="2"/><rect x="5" y="4" width="2" height="2"/><rect x="8" y="4" width="2" height="2"/><rect x="2" y="7" width="2" height="2"/><rect x="5" y="7" width="2" height="2"/><rect x="8" y="7" width="2" height="2"/></g></svg></div>
  <div class="opt" style="left:380px;top:155px"><span class="box" style="background:#fff;border:1px solid #333;position:relative"><svg style="position:absolute;left:0;top:0" width="9" height="9" viewBox="0 0 9 9"><path d="M1 4.5l2.5 2.5L8 1.5" fill="none" stroke="#333" stroke-width="1.8"/></svg></span>Back</div>
  <div class="opt" style="left:435px;top:155px"><span class="box"></span>One way</div>

  <div class="lbl left" style="top:179px">Passengers</div>
  <svg class="abs" style="left:102px;top:172px" width="10" height="28" viewBox="0 0 10 28"><circle cx="5" cy="3" r="3" fill="#222"/><path d="M1 8h8v10H7v10H3V18H1z" fill="#222"/></svg>
  <div class="sel" style="left:115px">1<i></i></div>
  <svg class="abs" style="left:160px;top:177px" width="8" height="20" viewBox="0 0 8 20"><circle cx="4" cy="2.5" r="2.5" fill="#222"/><path d="M1 6h6v7H5.5v7h-3v-7H1z" fill="#222"/></svg>
  <div class="sel" style="left:172px">1<i></i></div>
  <svg class="abs" style="left:218px;top:180px" width="10" height="16" viewBox="0 0 10 16"><circle cx="5" cy="3" r="3" fill="#222"/><ellipse cx="5" cy="11" rx="4" ry="5" fill="#222"/></svg>
  <div class="sel" style="left:231px">1<i></i></div>

  <div class="lbl right" style="top:180px">Class</div>
  <div class="field" style="left:370px;top:173px;width:166px">Economy<i></i></div>

  <div class="pill">July, 2013</div>
  <div class="search-btn">SEARCH</div>
</section>

<section class="services">
  <div class="service-head" style="left:210px">
    <svg class="abs" style="left:72px;top:14px" width="22" height="32" viewBox="0 0 22 32"><path d="M2 2h18v28H2z" fill="none" stroke="#fff" stroke-width="2"/><path d="M2 2l10 4v26L2 30z" fill="#fff"/></svg>
    <div class="name" style="left:104px">VISA INFO</div>
  </div>
  <div class="service-head" style="left:475px">
    <svg class="abs" style="left:72px;top:13px" width="34" height="34" viewBox="0 0 34 34"><rect x="8" y="8" width="18" height="18" transform="rotate(45 17 17)" fill="none" stroke="#fff" stroke-width="2.5"/><rect x="12" y="12" width="10" height="10" transform="rotate(45 17 17)" fill="none" stroke="#fff" stroke-width="1.5"/></svg>
    <div class="name" style="left:112px">TICKETS</div>
  </div>
  <div class="service-head" style="left:742px">
    <svg class="abs" style="left:78px;top:12px" width="24" height="36" viewBox="0 0 24 36"><path d="M8 2h8v6h6v28H2V8h6z" fill="#fff"/><g fill="#353535"><rect x="6" y="12" width="3" height="3"/><rect x="11" y="12" width="3" height="3"/><rect x="16" y="12" width="3" height="3"/><rect x="6" y="18" width="3" height="3"/><rect x="11" y="18" width="3" height="3"/><rect x="16" y="18" width="3" height="3"/><rect x="6" y="24" width="3" height="3"/><rect x="16" y="24" width="3" height="3"/><rect x="10" y="29" width="5" height="7"/></g></svg>
    <div class="name" style="left:112px">HOTELS</div>
  </div>

  <article class="service-card" style="left:209px">
    <h3>There Are Two Options Apply For A Visa</h3>
    <ol><li>1.&nbsp; Oformlenie visa “Online”</li><li>2.&nbsp; Visa “Myself.”</li></ol>
    <a class="more">Read More...</a>
  </article>
  <article class="service-card" style="left:474px">
    <h3>Flights From Tours Designer.</h3>
    <p style="top:49px">On our site you can consider offers from different airlines and purchase tickets according to your wishes and budget.</p>
    <a class="more" style="left:25px">Read More...</a>
  </article>
  <article class="service-card" style="left:741px">
    <h3>Hotels By City Builder.</h3>
    <p style="top:49px">Our site offers a wide selection of hotels located in different countries and continents of the world. You can choose and book all kinds of accommodation options, according to your wishes and budget.</p>
    <a class="more" style="left:17px">Read More...</a>
  </article>
</section>

<footer class="footer">
  <div class="col" style="left:214px"><h4>Navigation</h4><ul><li>HOME</li><li>ABOUT US</li><li>FORUM</li><li>CONTACTS</li></ul></div>
  <div class="vsep" style="left:310px"></div>
  <div class="col" style="left:332px"><h4>Help</h4><ul><li>HELP</li><li>TERMS OF USE</li><li>PRIVACY POLICY</li><li>COOKIES</li></ul></div>
  <div class="vsep" style="left:446px"></div>
  <div class="col" style="left:465px"><h4>Location</h4><address>Roamquiltex Limited<br>14 Harlow Mews<br>London, E2 0QX<br>UK</address></div>
  <div class="vsep" style="left:614px"></div>
  <div class="col" style="left:634px"><h4>Contact</h4><ul><li>+7 (495) 555-01-42</li><li>info@roamquiltex.com</li></ul><div class="social"><span></span><span></span><span></span><span></span><span></span></div></div>
  <div class="vsep" style="left:790px"></div>
  <div class="col" style="left:804px"><h4>Newsletter Subscription</h4><ul><li style="letter-spacing:.3px;height:14px">Subscribe to Our Free Promotions</li></ul></div>
</footer>
<div class="email">Enter Your Email Address</div>
<div class="subscribe">Subscribe</div>
<div class="copy">© 2013 <b>velmorytravel</b>. All rights reserved</div>

</body>
</html>
```